Home Loan Introducer needs logo/business cards

We need a simple but classy logo for business cards and flyers. The business is a home loan referral business that is called an Introducer. The business name is "The Pellgrove".
I was thinking very simple and straight to the point on the front with "Home Loans" the only thing on the front with a nice background colour/s.
Then on the back, "The Pellgrove"
and "Quality Customer Service"
and "Email, text or call welcome"
and then my name, email address and phone number.
Thank you for all the designs :-)
Home buyers.
Home owners.
Investors.
Loan

```html
<!DOCTYPE html>
<html lang="en">
<head>
<meta charset="utf-8">
<title>The Pellgrove — Business Card</title>
<link rel="stylesheet" href="https://fonts.googleapis.com/css2?family=Source+Sans+3:wght@400;600;700&display=swap">
<style>
  :root {
    --stage: #3a3a3c;
    --brand-green: #8dc63f;
    --ink: #111111;
    --paper: #ffffff;
  }
  * { margin: 0; padding: 0; box-sizing: border-box; }
  html, body {
    width: 1200px; height: 999px; overflow: hidden;
    background: var(--stage);
    font-family: "Source Sans 3", "Myriad Pro", Arial, sans-serif;
  }
  .canvas { position: relative; width: 1200px; height: 999px; }

  /* Front of card */
  .card-front {
    position: absolute; left: 140px; top: 46px;
    width: 779px; height: 445px;
    background: var(--brand-green);
    display: flex; align-items: center; justify-content: center; gap: 22px;
  }
  .card-front .brand-mark { width: 58px; height: 58px; background: var(--ink); }
  .card-front .brand-name {
    font-size: 76px; font-weight: 700; color: var(--ink);
    letter-spacing: -0.5px; line-height: 1;
  }

  /* Back of card */
  .card-back {
    position: absolute; left: 281px; top: 508px;
    width: 778px; height: 444px;
    background: var(--paper);
    overflow: hidden;
  }
  .card-back .panel-shape { position: absolute; left: 0; top: 0; }

  .brand-block { position: absolute; left: 32px; top: 105px; display: flex; align-items: center; gap: 14px; }
  .brand-block .brand-mark { width: 40px; height: 40px; background: var(--brand-green); }
  .brand-block .brand-name { font-size: 34px; font-weight: 400; color: var(--ink); line-height: 1; }
  .brand-block .tagline { font-size: 20px; color: var(--ink); line-height: 1.2; margin-top: 4px; }

  .person { position: absolute; left: 448px; top: 74px; color: var(--ink); }
  .person .name { font-size: 33px; font-weight: 400; line-height: 1.1; }
  .person .role { font-size: 18px; margin-top: 4px; }

  .panel-text {
    position: absolute; left: 448px; top: 226px;
    color: var(--paper); font-size: 19px; line-height: 26px;
  }
  .contact-list { list-style: none; margin-top: 28px; }
  .contact-list li { display: flex; align-items: center; height: 26px; }
  .contact-list .icon { width: 18px; height: 18px; margin-left: 2px; }
  .contact-list .sep { margin: 0 14px 0 22px; }
</style>
</head>
<body>
<main class="canvas">

  <section class="card-front" aria-label="Card front">
    <span class="brand-mark" aria-hidden="true"></span>
    <span class="brand-name">The Pellgrove</span>
  </section>

  <section class="card-back" aria-label="Card back">
    <svg class="panel-shape" width="778" height="444" viewBox="0 0 778 444" aria-hidden="true">
      <polygon fill="var(--brand-green)"
        points="433,165 761,165 761,387 729,418 0,418 0,408 351,408"/>
    </svg>

    <div class="brand-block">
      <span class="brand-mark" aria-hidden="true"></span>
      <div>
        <div class="brand-name">The Pellgrove</div>
        <div class="tagline">Quality Customer Service</div>
      </div>
    </div>

    <div class="person">
      <div class="name">Person Name</div>
      <div class="role">designation</div>
    </div>

    <div class="panel-text">
      <p>Lorem ipsum dolor sit amet,<br>consectetur adipiscing elit.<br>Donec accumsan.</p>
      <ul class="contact-list">
        <li>
          <svg class="icon" viewBox="0 0 18 18" aria-hidden="true"><path fill="#fff" d="M5 2 L8 5 L6 7 C7 10 8 11 11 12 L13 10 L16 13 L14 16 C8 16 2 10 2 4 Z"/></svg>
          <span class="sep">:</span><span>123 4564 7899</span>
        </li>
        <li>
          <svg class="icon" viewBox="0 0 18 18" aria-hidden="true"><rect x="1" y="4" width="16" height="11" fill="#fff"/><path d="M1 4 L9 10 L17 4" stroke="var(--brand-green)" stroke-width="1.4" fill="none"/></svg>
          <span class="sep">:</span><span>hello@pellgrove.com</span>
        </li>
        <li>
          <svg class="icon" viewBox="0 0 18 18" aria-hidden="true"><path fill="#fff" d="M16 2 L2 8 L8 10 L10 16 Z"/></svg>
          <span class="sep">:</span><span>pellgrove.com</span>
        </li>
      </ul>
    </div>
  </section>

</main>
</body>
</html>
```